Job Coaching - Mova; engaging people to improve their work experience

design a website focussed on people
with 4 tabs/pages (+2)
1) landing page
2) Professional
3) Job Coaching
4) Bio
5) Contact
6) references

I've added the text to be used in the documents. The website will be in Dutch, but I've added the translations in green just for you to understand what it is about.

I've added my logo as well, and a flyer I used already. this gives you an idea on how it could look like
Pictures you can find there as well. Other pictures can be added of course
The techical creation of the website is not needed. I need all the designs and information to be able to create it myself.

```html
<!DOCTYPE html>
<html lang="en">
<head>
<meta charset="utf-8">
<title>Mova Professional Coaching</title>
<link href="https://fonts.googleapis.com/css2?family=Open+Sans:wght@400;600&family=Poppins:wght@300;400;500;600;700;800&display=swap" rel="stylesheet">
<style>
:root{
  --teal:#2e9e94;
  --teal-deep:#1b7a96;
  --grey-bar:#6b6b6b;
  --text:#3a3a3a;
  --white:#ffffff;
}
*{margin:0;padding:0;box-sizing:border-box}
html,body{width:1057px;height:1200px;overflow:hidden;background:var(--white)}
body{position:relative;font-family:'Poppins',sans-serif;color:var(--text)}
.topbar{position:absolute;left:288px;top:0;width:769px;height:38px;background:var(--grey-bar);
  clip-path:polygon(0 0,100% 0,100% 100%,34px 100%);color:var(--white);font-family:'Open Sans',sans-serif}
.topbar .item{position:absolute;top:8px;font-size:17px;display:flex;align-items:center;gap:10px;white-space:nowrap}
.topbar .phone{left:150px}
.topbar .mail{left:375px}
.topbar .lang{left:589px;top:4px;font-size:13px;gap:6px}
.flag{width:30px;height:30px;border-radius:50%;background:linear-gradient(#c8102e 0 14%,#fff 14% 28%,#c8102e 28% 42%,#fff 42% 56%,#c8102e 56% 70%,#fff 70% 84%,#c8102e 84%);position:relative;overflow:hidden}
.flag::before{content:"";position:absolute;left:0;top:0;width:14px;height:14px;background:#2a3f8f}
.brand{position:absolute;left:84px;top:22px;display:flex;align-items:center;gap:10px}
.brand .dot{width:46px;height:46px;border-radius:50%;background:var(--teal)}
.brand .name{font-size:42px;font-weight:600;color:var(--teal);letter-spacing:2px;line-height:1}
.nav{position:absolute;top:52px;left:326px;display:flex;gap:33px;font-family:'Open Sans',sans-serif;font-size:17.5px;color:#333}
.hero{position:absolute;left:0;top:109px;width:1057px;height:480px;
  background:radial-gradient(ellipse at 40% 35%,#1eaed0 0%,#1a96b8 55%,#155f78 100%)}
.hero-scene{position:absolute;left:0;top:0;width:1057px;height:480px}
.hero-copy{position:absolute;left:494px;top:88px;color:var(--white)}
.hero-copy .welcome{font-size:20px;font-weight:400}
.hero-copy .title{font-size:82px;font-weight:800;line-height:1;margin-top:6px;letter-spacing:1px}
.hero-copy .sub{font-size:23px;font-weight:600;margin-top:10px;letter-spacing:.3px}
.btn{position:absolute;left:494px;top:252px;width:138px;height:42px;background:#5f5f5f;color:var(--white);
  font-size:18px;font-weight:500;display:flex;align-items:center;justify-content:center;box-shadow:2px 3px 5px rgba(0,0,0,.3)}
.wave{position:absolute;left:0;top:440px}
.points{position:absolute;left:60px;top:630px;width:490px;list-style:none}
.points li{position:relative;padding-left:27px;font-size:12.5px;line-height:24px;margin-bottom:24px;font-weight:300;color:#333}
.points li svg{position:absolute;left:0;top:6px}
.portrait-ring{position:absolute;left:650px;top:575px}
.portrait{position:absolute;left:655px;top:590px;width:332px;height:332px;border-radius:50%;
  background:linear-gradient(135deg,#b89a80 0%,#a86a5a 50%,#8e2c3a 100%)}
.cta{position:absolute;left:0;top:1021px;width:1057px;height:105px;background:var(--teal-deep);display:flex;align-items:center;justify-content:center}
.cta a{color:var(--white);font-size:18px;text-decoration:underline;text-underline-offset:5px;text-decoration-thickness:1px}
.footer{position:absolute;left:0;top:1158px;width:1057px;text-align:center;font-family:'Open Sans',sans-serif;font-size:16px;color:#333}
</style>
</head>
<body>
<div class="topbar">
  <div class="item phone"><svg width="16" height="16" viewBox="0 0 24 24"><path fill="#fff" d="M6.6 10.8a15 15 0 0 0 6.6 6.6l2.2-2.2c.3-.3.7-.4 1-.2 1.1.4 2.3.6 3.6.6.6 0 1 .4 1 1V20c0 .6-.4 1-1 1A17 17 0 0 1 3 4c0-.6.4-1 1-1h3.5c.6 0 1 .4 1 1 0 1.3.2 2.5.6 3.6.1.3 0 .7-.2 1z"/></svg>+1 555-010-0147</div>
  <div class="item mail"><svg width="18" height="14" viewBox="0 0 18 14"><rect x="1" y="1" width="16" height="12" rx="1.5" fill="none" stroke="#fff" stroke-width="1.6"/><path d="M1.5 2l7.5 6 7.5-6" fill="none" stroke="#fff" stroke-width="1.6"/></svg>info@mova.com</div>
  <div class="item lang">EN - <span class="flag"></span></div>
</div>

<div class="brand"><span class="dot"></span><span class="name">MOVA</span></div>

<nav class="nav"><span>Home</span><span>Professional</span><span>Job Coaching</span><span>Bio</span><span>Contact</span><span>References</span></nav>

<section class="hero">
  <div class="hero-scene" role="img" aria-label="Wooden cut-out figure climbing wooden block steps while a hand places the next block, on a blue background"></div>
  <div class="hero-copy">
    <div class="welcome">Welcome to</div>
    <div class="title">MOVA</div>
    <div class="sub">PROFESSIONAL COACHING</div>
  </div>
  <div class="btn">Get Started</div>
</section>

<svg class="wave" width="1057" height="160" viewBox="0 0 1057 160">
  <path d="M0 124 C120 150 300 150 470 90 C620 30 700 15 800 18 C900 22 1000 40 1057 60 L1057 160 L0 160 Z" fill="#fff"/>
  <path d="M0 124 C120 150 300 150 470 90 C620 30 700 15 800 18 C900 22 1000 40 1057 60" fill="none" stroke="#2e9e94" stroke-width="4"/>
</svg>

<ul class="points">
  <li><svg width="12" height="12" viewBox="0 0 12 12"><circle cx="6" cy="6" r="6" fill="#2e9e94"/><path d="M5 3.5 7.5 6 5 8.5" fill="none" stroke="#fff" stroke-width="1.6"/></svg>Hello, my name is Jonas Verlinden. As a passionate career coach, I want to empower you to do your job every day.</li>
  <li><svg width="12" height="12" viewBox="0 0 12 12"><circle cx="6" cy="6" r="6" fill="#2e9e94"/><path d="M5 3.5 7.5 6 5 8.5" fill="none" stroke="#fff" stroke-width="1.6"/></svg>We are staying at work longer and longer, so today more than ever it is important to pay the necessary attention to professional growth and well-being at work.</li>
  <li><svg width="12" height="12" viewBox="0 0 12 12"><circle cx="6" cy="6" r="6" fill="#2e9e94"/><path d="M5 3.5 7.5 6 5 8.5" fill="none" stroke="#fff" stroke-width="1.6"/></svg>I am convinced that people are often capable of more than they believe themselves to be. Everything starts with the desire for change. Who am I? What is my role? What do I really want?</li>
  <li><svg width="12" height="12" viewBox="0 0 12 12"><circle cx="6" cy="6" r="6" fill="#2e9e94"/><path d="M5 3.5 7.5 6 5 8.5" fill="none" stroke="#fff" stroke-width="1.6"/></svg>As a job coach, I don't go for simple quick-wins or ready-made tips and tricks. In a spirit of openness, trust and equality, we search together for the deeper insights and sustainable solutions that work for you. Coaching is an awareness process that leads to finding the answers within yourself.</li>
</ul>

<svg class="portrait-ring" width="360" height="360" viewBox="0 0 360 360">
  <path d="M83 28 A176 176 0 0 1 347 181" fill="none" stroke="#1b7a96" stroke-width="8"/>
</svg>
<div class="portrait" role="img" aria-label="Portrait photo of the coach in a red shirt, standing indoors"></div>

<div class="cta"><a href="#">Sign up today for a no-obligation introductory consultation and take control of your career (again).</a></div>

<footer class="footer">© Copyrights 2023 Mova |&nbsp; All Rights Reserved</footer>
</body>
</html>
```